Redesign our Product Box!

We have a product box for our pet supplement we are looking to redesign. Please use the photoshop file of the current design for the logo/info/dieline and the concept picture of a bag we would like to see included in the box design.

Ideally the background will be the green with white text, but we really want it to be fun and appealing to pet owners so do not be scared to show your vision.

```html
<!DOCTYPE html>
<html lang="en">
<head>
<meta charset="utf-8">
<title>VerdaPlankton – Carton Dieline</title>
<link rel="stylesheet" href="https://fonts.googleapis.com/css2?family=Source+Sans+3:wght@400;600;700&family=Archivo:wght@800&display=swap">
<style>
  :root {
    --brand-green: #00a649;
    --ink-white: #ffffff;
    --cut-line: #c8332b;
    --fold-line: #3f58b8;
    --ink-dark: #111111;
    --paper: #ffffff;
    --swoosh-light: #ffffff;
    --swoosh-shade: #dcdcdc;
  }
  html, body {
    margin: 0;
    padding: 0;
    width: 1200px;
    height: 1200px;
    overflow: hidden;
    background: var(--paper);
  }
  .dieline { display: block; width: 1200px; height: 1200px; }
  .panel { fill: var(--brand-green); stroke: var(--cut-line); stroke-width: 0.8; }
  .fold { stroke: var(--fold-line); stroke-width: 0.6; fill: none; }
  .txt { font-family: "Source Sans 3", "Myriad Pro", sans-serif; fill: var(--ink-white); }
  .brand-name { font-weight: 700; font-size: 27px; letter-spacing: -0.5px; }
  .tagline { font-size: 14.5px; }
  .net-weight { font-size: 11px; }
  .body-copy { font-size: 10px; }
  .body-head { font-size: 11.5px; font-weight: 600; }
  .print-side { font-family: "Source Sans 3", sans-serif; font-size: 26px; fill: var(--ink-dark); }
  .facts-box { fill: var(--paper); }
  .facts-title { font-family: "Archivo", Arial, sans-serif; font-weight: 800; font-size: 17px; fill: var(--ink-dark); }
  .facts-small { font-family: "Source Sans 3", Arial, sans-serif; font-size: 6px; fill: var(--ink-dark); }
  .facts-tiny { font-family: "Source Sans 3", Arial, sans-serif; font-size: 4.2px; fill: #444; }
  .facts-rule { stroke: var(--ink-dark); }
  .distributor { font-size: 9.5px; }
  .distributor-head { font-size: 9.5px; font-weight: 700; }
  .warning-copy { font-size: 5.6px; }
  .lot-code { font-size: 12px; }
</style>
</head>
<body>
<svg class="dieline" viewBox="512 1050 860 870" xmlns="http://www.w3.org/2000/svg">
  <defs>
    <linearGradient id="swooshFill" x1="0" y1="0" x2="1" y2="0">
      <stop offset="0" stop-color="var(--swoosh-light)"/>
      <stop offset="1" stop-color="var(--swoosh-shade)"/>
    </linearGradient>
  </defs>

  <!-- structure -->
  <g class="carton-structure">
    <path class="panel top-tuck" d="M590,1130 L590,1112 Q598,1070 626,1065 L768,1065 Q796,1072 800,1130 Z"/>
    <rect class="panel top-panel" x="590" y="1130" width="210" height="168"/>
    <polygon class="panel glue-flap" points="537,1303 590,1298 590,1677 537,1673"/>
    <rect class="panel front-panel" x="590" y="1298" width="212" height="379"/>
    <polygon class="panel dust-flap" points="802,1183 948,1183 955,1275 968,1285 968,1298 802,1298"/>
    <rect class="panel side-panel" x="802" y="1298" width="166" height="379"/>
    <rect class="panel back-panel" x="968" y="1298" width="214" height="379"/>
    <polygon class="panel dust-flap" points="1200,1183 1347,1183 1347,1298 1182,1298 1182,1285 1195,1275"/>
    <rect class="panel side-panel" x="1182" y="1298" width="165" height="379"/>
    <polygon class="panel dust-flap" points="805,1677 968,1677 968,1795 822,1795 815,1705 805,1695"/>
    <polygon class="panel dust-flap" points="1182,1677 1347,1677 1347,1695 1337,1705 1328,1795 1182,1795"/>
    <rect class="panel bottom-panel" x="970" y="1677" width="210" height="168"/>
    <path class="panel bottom-tuck" d="M972,1845 L1178,1845 L1178,1870 Q1165,1905 1140,1912 L1010,1912 Q980,1905 972,1870 Z"/>
    <line class="fold" x1="590" y1="1130" x2="800" y2="1130"/>
    <line class="fold" x1="590" y1="1298" x2="1347" y2="1298"/>
    <line class="fold" x1="537" y1="1677" x2="1347" y2="1677"/>
    <line class="fold" x1="590" y1="1298" x2="590" y2="1677"/>
    <line class="fold" x1="802" y1="1298" x2="802" y2="1677"/>
    <line class="fold" x1="968" y1="1298" x2="968" y2="1677"/>
    <line class="fold" x1="1182" y1="1298" x2="1182" y2="1677"/>
    <line class="fold" x1="970" y1="1845" x2="1180" y2="1845"/>
  </g>

  <text class="print-side" x="1075" y="1214" text-anchor="middle">PRINT</text>
  <text class="print-side" x="1068" y="1249" text-anchor="middle">SIDE</text>

  <!-- top panel -->
  <text class="txt brand-name" x="695" y="1209" text-anchor="middle">VerdaPlankton</text>

  <!-- front panel -->
  <g class="front-face">
    <text class="txt brand-name" x="693" y="1366" text-anchor="middle">VerdaPlankton</text>
    <text class="txt tagline" x="693" y="1409" text-anchor="middle">Foundational Nutrition</text>
    <text class="txt tagline" x="693" y="1428" text-anchor="middle">&amp; Super-Antioxidant</text>
    <text class="txt tagline" x="693" y="1478" text-anchor="middle">For Dogs &amp; Cats</text>
    <g role="img" aria-label="Flowing white feather-like swoosh graphic">
      <path d="M593,1520 L787,1490 L787,1620 L593,1620 Z" fill="url(#swooshFill)"/>
    </g>
    <text class="txt net-weight" x="695" y="1654" text-anchor="middle">15g</text>
  </g>

  <!-- side panel: directions -->
  <g class="txt body-copy directions" text-anchor="middle">
    <text x="886" y="1322">Directions: For dogs &amp; cats</text>
    <text x="886" y="1336">1/16tsp once per day.</text>
    <text x="886" y="1350">Administer orally. To be mixed</text>
    <text x="886" y="1364">into food. 1/16tsp = 1/2 the</text>
    <text x="886" y="1378">included scoop.</text>
    <line x1="828" y1="1400" x2="945" y2="1400" stroke="var(--ink-white)" stroke-width="0.8"/>
    <text class="body-head" x="886" y="1415">Unlock Nature’s</text>
    <text class="body-head" x="886" y="1432">Nutrient Treasure:</text>
    <text x="886" y="1459">Phytoplankton is the foundation of</text>
    <text x="886" y="1473">life, It is the first plant in the entire</text>
    <text x="886" y="1487">food chain.</text>
    <text x="886" y="1515">Phytoplankton is a microscopic</text>
    <text x="886" y="1529">powerhouse. Your pet’s body</text>
    <text x="886" y="1543">absorbs billions of phytoplankton</text>
    <text x="886" y="1557">with every serving.</text>
    <text x="886" y="1585">Packed with the building blocks of</text>
    <text x="886" y="1599">life, phytoplankton addresses</text>
    <text x="886" y="1613">multiple aspects of your pet’s</text>
    <text x="886" y="1627">health in one simple supplement.</text>
  </g>

  <!-- back panel: supplement facts -->
  <g class="supplement-facts">
    <rect class="facts-box" x="976" y="1308" width="200" height="155"/>
    <rect x="981" y="1313" width="190" height="99" fill="none" class="facts-rule" stroke-width="1"/>
    <text class="facts-title" x="1072" y="1333" text-anchor="middle">Supplement Facts</text>
    <line class="facts-rule" x1="981" y1="1340" x2="1171" y2="1340" stroke-width="2"/>
    <text class="facts-small" x="993" y="1350">Serving Size: 1 Scoop/Day</text>
    <text class="facts-small" x="993" y="1358">Servings per Container: 30</text>
    <text class="facts-small" x="1085" y="1358">Amount per Serving</text>
    <text class="facts-small" x="1150" y="1358">%DV</text>
    <line class="facts-rule" x1="981" y1="1364" x2="1171" y2="1364" stroke-width="1.5"/>
    <text class="facts-small" x="993" y="1380">Microalgae Nannochloropsis Gaditana</text>
    <text class="facts-small" x="1124" y="1380">500mg</text>
    <text class="facts-small" x="1156" y="1380">‡</text>
    <line class="facts-rule" x1="981" y1="1391" x2="1171" y2="1391" stroke-width="1.5"/>
    <text class="facts-small" x="993" y="1404">‡ Daily value not established.</text>
    <text class="facts-tiny" x="981" y="1421">These statements have not been evaluated by the Food and Drug Administration.</text>
    <text class="facts-tiny" x="981" y="1428">This product is not intended to diagnose, treat, cure, or prevent any disease.</text>
    <text class="facts-tiny" x="981" y="1443">Store in a cool, dry place.</text>
  </g>

  <g class="txt distributor-block">
    <text class="distributor-head" x="983" y="1491">Distributed By::</text>
    <text class="distributor" x="983" y="1503">Marisol Pet Nutrition Inc.</text>
    <text class="distributor" x="983" y="1516">42 Harbour Lane,</text>
    <text class="distributor" x="983" y="1529">Port Elden, Nova Scotia Canada</text>
    <text class="distributor" x="983" y="1542">B0A 1C0</text>
    <text class="warning-copy" x="983" y="1554">Warnings: Check with a qualified healthcare professional before</text>
    <text class="warning-copy" x="983" y="1561">using this product if you are pregnant, breastfeeding, or taking</text>
    <text class="warning-copy" x="983" y="1568">blood thinners. You should call your doctor for medical advice</text>
    <text class="warning-copy" x="983" y="1575">about serious adverse events. To report a serious adverse event</text>
    <text class="warning-copy" x="983" y="1582">or obtain product information contact: 1 800 555 0142</text>
  </g>

  <!-- side panel: story -->
  <g class="txt body-copy product-story" text-anchor="middle">
    <text x="1262" y="1322">Our premium phytoplankton</text>
    <text x="1262" y="1336">powder is a extraordinary</text>
    <text x="1262" y="1350">supplement.  It infuses your pet’s</text>
    <text x="1262" y="1364">body with pure, plant-based</text>
    <text x="1262" y="1378">nutrients and potent antioxidants.</text>
    <text x="1262" y="1406">Phytoplankton goes beyond</text>
    <text x="1262" y="1420">ordinary supplements; it’s a path</text>
    <text x="1262" y="1434">to optimal health. In just a few</text>
    <text x="1262" y="1448">weeks, your pet will experience a</text>
    <text x="1262" y="1462">feeling of calm and strength, the</text>
    <text x="1262" y="1476">kind of wellness our customers</text>
    <text x="1262" y="1490">often say they’ve been seeking.</text>
    <text x="1262" y="1518">Join those who have discovered</text>
    <text x="1262" y="1532">the transformative power of</text>
    <text x="1262" y="1546">phytoplankton. See the difference</text>
    <text x="1262" y="1560">for yourself and understand why</text>
    <text x="1262" y="1574">it’s not just a supplement, but a</text>
    <text x="1262" y="1588">revolution in pet health and</text>
    <text x="1262" y="1602">vitality.</text>
  </g>

  <!-- bottom panel lot code -->
  <text class="txt lot-code" x="1077" y="1822" text-anchor="middle" transform="rotate(180 1077 1818)">Exp: 2025/03/Lot No:12222</text>
</svg>
</body>
</html>
```